Worksheet for a seminar - wheel of wellbeing

I need a 1 page worksheet for a course I am running next week.
1. The worksheet is based is designed to tie into Dorvelle who use 4 colours per specific quadrants - Blue top left, Yellow top right, Green bottom left, Red bottom right. As this is designed to be written and to be printed, it may need to be pale colours however I am open to the correct colours with the image on top if necessary

2. The wellbeing wheel needs to be a design of it's own as it will be used in other things. I would like to have a format for the base wheel that can be changed by me (Only the title names)

3. I have provided the 2 business logo's - these down need to be too big

I hope this helps.

Corporate managers and staff - worksheet being used in a workshop

Wheel

• A professional looking wheel that can be used for other purposes. I want to be able to change the 'pie' titles. I will also require a A4 size of the wheel with blank spaces for titles
• A modern feel

```html
<!DOCTYPE html>
<html lang="en">
<head>
<meta charset="utf-8">
<title>Wheel of Wellbeing Worksheet</title>
<link href="https://fonts.googleapis.com/css2?family=Lato:wght@400;700;900&display=swap" rel="stylesheet">
<style>
  :root {
    --backdrop: #1e1e1e;
    --paper: #ffffff;
    --blue: #0a8fcf;
    --yellow: #fde725;
    --green: #35b152;
    --red: #ef5343;
    --wheel-green: #2a8b41;
    --wheel-orange: #da5b37;
    --wheel-teal: #56c0a7;
    --title-red: #e8474a;
    --date-green: #3aa84b;
    --logo-green: #5ea83a;
    --logo-teal: #3aa68c;
  }
  * { box-sizing: border-box; margin: 0; padding: 0; }
  html, body { width: 1200px; height: 1200px; overflow: hidden; }
  body { background: var(--backdrop); font-family: "Lato", sans-serif; position: relative; }

  .worksheet { position: absolute; left: 215px; top: 58px; width: 768px; height: 1086px; background: var(--paper); }
  .quadrant { position: absolute; width: 378px; }
  .quadrant--assess { left: 0; top: 16px; height: 520px; background: var(--blue); }
  .quadrant--goals { left: 390px; top: 16px; height: 520px; background: var(--yellow); }
  .quadrant--action { left: 0; top: 550px; height: 536px; background: var(--green); }
  .quadrant--reflect { left: 390px; top: 550px; height: 536px; background: var(--red); }

  .brand { position: absolute; top: 0; height: 109px; background: var(--paper); display: flex; align-items: center; justify-content: center; gap: 10px; font-weight: 900; font-size: 38px; }
  .brand--assess { left: 51px; width: 266px; color: var(--logo-green); }
  .brand--goals { left: 63px; width: 265px; height: 113px; color: var(--logo-teal); }
  .brand__dot { width: 16px; height: 16px; border-radius: 50%; background: currentColor; }

  .step-title { position: absolute; font-size: 24px; font-weight: 700; line-height: 26px; color: var(--paper); }
  .quadrant--assess .step-title { left: 19px; top: 138px; }
  .quadrant--goals .step-title { left: 12px; top: 138px; color: var(--title-red); }
  .step-title__indent { padding-left: 29px; }
  .quadrant--action .step-title { left: 21px; top: 10px; }
  .quadrant--reflect .step-title { left: 15px; top: 10px; }

  .wheel { position: absolute; left: 67px; top: 209px; width: 244px; height: 244px; }

  .date-label { position: absolute; left: 18px; top: 478px; font-size: 24px; line-height: 28px; font-weight: 700; color: var(--paper); }
  .quadrant--goals .date-label { left: 15px; color: var(--date-green); }

  .column-head { position: absolute; top: 45px; font-size: 24px; font-weight: 700; color: var(--paper); }
  .column-head--action { left: 50px; }
  .column-head--when { left: 263px; }

  .answer-box { position: absolute; left: 18px; width: 340px; height: 75px; border-radius: 13px; overflow: hidden; background: linear-gradient(to right, var(--paper) 0 232px, var(--yellow) 232px 100%); }
  .quadrant--reflect .answer-box { left: 12px; }

  .question { position: absolute; left: 12px; font-size: 15px; font-weight: 700; line-height: 22px; color: var(--paper); }
</style>
</head>
<body>
<main class="worksheet">

  <section class="quadrant quadrant--assess">
    <div class="brand brand--assess"><span class="brand__dot"></span>Herrmnan</div>
    <h2 class="step-title">1) Access where are you now?</h2>
    <svg class="wheel" viewBox="-122 -122 244 244" aria-label="Wellbeing wheel">
      <g stroke="#fff" stroke-width="1.5">
        <path d="M0 0 L-31.6 -117.8 A122 122 0 0 1 61 -105.7Z" fill="var(--wheel-green)"/>
        <path d="M0 0 L61 -105.7 A122 122 0 0 1 117.8 -31.6Z" fill="var(--wheel-orange)"/>
        <path d="M0 0 L117.8 -31.6 A122 122 0 0 1 105.7 61Z" fill="var(--yellow)"/>
        <path d="M0 0 L105.7 61 A122 122 0 0 1 31.6 117.8Z" fill="var(--blue)"/>
        <path d="M0 0 L31.6 117.8 A122 122 0 0 1 -61 105.7Z" fill="var(--wheel-green)"/>
        <path d="M0 0 L-61 105.7 A122 122 0 0 1 -117.8 31.6Z" fill="var(--wheel-orange)"/>
        <path d="M0 0 L-117.8 31.6 A122 122 0 0 1 -105.7 -61Z" fill="var(--yellow)"/>
        <path d="M0 0 L-105.7 -61 A122 122 0 0 1 -31.6 -117.8Z" fill="var(--blue)"/>
      </g>
      <g font-family="Lato, sans-serif" font-size="9" fill="#fff" text-anchor="middle" dominant-baseline="middle">
        <text transform="rotate(-82.5)" x="64">Physical Health</text>
        <text transform="rotate(-37.5)" x="68">Emotional Health</text>
        <text transform="rotate(7.5)" x="68" fill="var(--title-red)">Spiritual</text>
        <text transform="rotate(52.5)" x="68">Love Relationship</text>
        <text transform="rotate(-82.5)" x="-70">Family</text>
        <text transform="rotate(-37.5)" x="-72">Social</text>
        <text transform="rotate(7.5)" x="-72" fill="var(--title-red)">Personal Growth</text>
        <text transform="rotate(52.5)" x="-64">Business Career Study</text>
      </g>
    </svg>
    <p class="date-label">Date:</p>
  </section>

  <section class="quadrant quadrant--goals">
    <div class="brand brand--goals"><span class="brand__dot"></span>Dorvelle</div>
    <h2 class="step-title">3) Outcomes Goals where do<br><span class="step-title__indent">you want to be?</span></h2>
    <svg class="wheel" viewBox="-122 -122 244 244" aria-label="Wellbeing wheel goals">
      <g stroke="#fff" stroke-width="1.5">
        <path d="M0 0 L-31.6 -117.8 A122 122 0 0 1 61 -105.7Z" fill="var(--wheel-green)"/>
        <path d="M0 0 L61 -105.7 A122 122 0 0 1 117.8 -31.6Z" fill="var(--wheel-orange)"/>
        <path d="M0 0 L117.8 -31.6 A122 122 0 0 1 105.7 61Z" fill="var(--wheel-teal)"/>
        <path d="M0 0 L105.7 61 A122 122 0 0 1 31.6 117.8Z" fill="var(--blue)"/>
        <path d="M0 0 L31.6 117.8 A122 122 0 0 1 -61 105.7Z" fill="var(--wheel-green)"/>
        <path d="M0 0 L-61 105.7 A122 122 0 0 1 -117.8 31.6Z" fill="var(--wheel-orange)"/>
        <path d="M0 0 L-117.8 31.6 A122 122 0 0 1 -105.7 -61Z" fill="var(--wheel-teal)"/>
        <path d="M0 0 L-105.7 -61 A122 122 0 0 1 -31.6 -117.8Z" fill="var(--blue)"/>
      </g>
      <g font-family="Lato, sans-serif" font-size="9" fill="#fff" text-anchor="middle" dominant-baseline="middle">
        <text transform="rotate(-82.5)" x="64">Physical Health</text>
        <text transform="rotate(-37.5)" x="68">Emotional Health</text>
        <text transform="rotate(7.5)" x="68">Spiritual</text>
        <text transform="rotate(52.5)" x="68">Love Relationship</text>
        <text transform="rotate(-82.5)" x="-70">Family</text>
        <text transform="rotate(-37.5)" x="-72">Social</text>
        <text transform="rotate(7.5)" x="-72">Personal Growth</text>
        <text transform="rotate(52.5)" x="-64">Business Career Study</text>
      </g>
    </svg>
    <p class="date-label">Date Achieved By:</p>
  </section>

  <section class="quadrant quadrant--action">
    <h2 class="step-title">4) Action Plan</h2>
    <p class="column-head column-head--action">Action</p>
    <p class="column-head column-head--when">When</p>
    <div class="answer-box" style="top:78px"></div>
    <div class="answer-box" style="top:193px"></div>
    <div class="answer-box" style="top:313px"></div>
    <div class="answer-box" style="top:431px"></div>
  </section>

  <section class="quadrant quadrant--reflect">
    <h2 class="step-title">2) Reflect</h2>
    <p class="question" style="top:49px">Are there any surpriseds in your wheel?</p>
    <div class="answer-box" style="top:73px"></div>
    <p class="question" style="top:163px">What wellbeing gaps stand out as being<br>most important</p>
    <div class="answer-box" style="top:208px"></div>
    <p class="question" style="top:300px">How do you feel about it?</p>
    <div class="answer-box" style="top:322px"></div>
    <p class="question" style="top:413px">How might this affect your homelife/worklife</p>
    <div class="answer-box" style="top:437px"></div>
  </section>

</main>
</body>
</html>
```